" A Lunar Petal Studio é uma pequena empresa, localizada nos Estados Unidos, especializada em criar produtos personalizados para celebrações, como cake toppers, papelaria para festas e peças em papel, acrílico e madeira cortadas a laser. Cada produto é desenvolvido sob encomenda, com foco em qualidade, delicadeza e atenção aos detalhes, proporcionando uma experiência única e memorável para cada cliente. "

```html
<!DOCTYPE html>
<html lang="pt">
<head>
<meta charset="utf-8">
<title>Lunar Petal Studio — Papel Timbrado</title>
<link href="https://fonts.googleapis.com/css2?family=Montserrat:wght@400;500&display=swap" rel="stylesheet">
<style>
  :root {
    --stage: #efece8;
    --paper: #e7eefa;
    --ink: #5a4a46;
    --ink-soft: #8a7b77;
    --blush: #e9b7ab;
    --blush-deep: #d79b8d;
    --check-a: #d6e0f1;
    --check-b: #f3f6fc;
    --petal-circle: #f6e3dc;
  }
  * { margin: 0; padding: 0; box-sizing: border-box; }
  html, body { width: 1200px; height: 1200px; overflow: hidden; }
  body {
    background: var(--stage);
    font-family: "Montserrat", sans-serif;
    color: var(--ink);
    position: relative;
  }
  .letterhead {
    position: absolute;
    left: 187px;
    top: 40px;
    width: 826px;
    height: 1120px;
    background: var(--paper);
    box-shadow: 0 6px 22px rgba(60, 40, 30, 0.18);
    overflow: hidden;
  }
  .side-stripe {
    position: absolute;
    top: 0;
    bottom: 0;
    left: 768px;
    width: 14px;
    background: var(--blush);
    border-left: 2px solid var(--blush-deep);
    border-right: 2px solid var(--blush-deep);
  }
  .side-rule {
    position: absolute;
    top: 0;
    bottom: 0;
    left: 800px;
    width: 2px;
    background: var(--blush);
  }
  .brand {
    position: absolute;
    top: 82px;
    left: 0;
    width: 768px;
    display: flex;
    justify-content: center;
    align-items: center;
    gap: 18px;
  }
  .brand-mark {
    width: 76px;
    height: 76px;
    border-radius: 50%;
    background: var(--petal-circle);
    border: 2px solid #fff;
  }
  .brand-text { display: flex; flex-direction: column; align-items: center; }
  .brand-name {
    font-size: 28px;
    font-weight: 500;
    color: var(--ink);
    letter-spacing: 0.5px;
  }
  .brand-tagline {
    margin-top: 6px;
    font-size: 11px;
    font-weight: 500;
    color: var(--ink);
    letter-spacing: 2px;
    text-transform: uppercase;
  }
  .pattern-band {
    position: absolute;
    left: 0;
    width: 768px;
    top: 960px;
    height: 86px;
    background: linear-gradient(180deg, var(--check-a), var(--check-b));
  }
  .footer {
    position: absolute;
    top: 1076px;
    left: 0;
    width: 768px;
    font-size: 15px;
    color: var(--ink-soft);
  }
  .contact {
    position: absolute;
    display: flex;
    align-items: center;
    gap: 8px;
  }
  .contact-phone { left: 176px; }
  .contact-social { left: 432px; }
  .contact-dot {
    width: 14px; height: 14px;
    border: 1.5px solid var(--ink-soft);
    border-radius: 50%;
  }
</style>
</head>
<body>
  <main class="letterhead">
    <div class="side-stripe"></div>
    <div class="side-rule"></div>

    <header class="brand">
      <div class="brand-mark"></div>
      <div class="brand-text">
        <span class="brand-name">Lunar Petal Studio</span>
        <span class="brand-tagline">Handmade Celebrations</span>
      </div>
    </header>

    <div class="pattern-band" role="img" aria-label="Faixa decorativa xadrez em tons de azul claro"></div>

    <footer class="footer">
      <div class="contact contact-phone">
        <svg width="16" height="16" viewBox="0 0 24 24" aria-hidden="true">
          <path d="M6.6 10.8a15.1 15.1 0 0 0 6.6 6.6l2.2-2.2a1 1 0 0 1 1-.25 11.4 11.4 0 0 0 3.6.57 1 1 0 0 1 1 1V20a1 1 0 0 1-1 1A17 17 0 0 1 3 4a1 1 0 0 1 1-1h3.5a1 1 0 0 1 1 1c0 1.25.2 2.45.57 3.57a1 1 0 0 1-.25 1z" fill="none" stroke="#8a7b77" stroke-width="1.8"/>
        </svg>
        <span>(201) 555-0148</span>
      </div>
      <div class="contact contact-social">
        <span class="contact-dot"></span>
        <span>@lunarpetal.studio</span>
      </div>
    </footer>
  </main>
</body>
</html>
```